依頼概要
初めまして。本書は、会社等の会議を実施する立場の人に向けてのものと
なっております。
■依頼の目的/概要
lumora出版、ビジネスパーソン向け書籍の表紙デザインをお願いします。
今のところ、題名は
「だれでも週末から家庭菜園がはかどる」

■本の内容
会社等で、会議をうまく進めていきたいがなかなか思うように
薦められない方向けに、誰でも簡単にこれだけのことを実践すれば
会議が上手く進められるというポイントをまとめたものになっております。

■デザイン要望
ビジネスパーソン向けですが、会議等に不慣れな方向けで
あまり難しく考えなくても、誰でも簡単にトライできるという
イメージを持ってもらえるようにしたいです。

現在、原稿は9割がたできております。添付ファイルをご参照ください。

その他何かご不明な点がございましたら、お気軽にご質問下さい。
よろしくお願いいたします。
名前は、ペンネームにする予定です。
今のところ、柚木 瑛之助が候補です。
■ 選んだ理由

私のイメージする会社内での和気あいあいとした雰囲気のイラストがまずは
気に入りました。
ターゲットが、会議がうまくできない人向けなので、なるべくそれを意識して
親しみやすいものを選びました。

■ 提案者全員のお礼・コメント

今回は、ターゲットが初心者向けであったので、親しみやすいものを選びましたが、
例えば、会議を上から見たイラストなどは、斬新なアイデアで印象深く
ターゲットが違えば、選んでいたと思います。
中身を理解して、提案いただけた方も多く、感謝いたします。
今後も、このシリーズを出版していきたいと考えておりますので
次の機会もよろしくお願いいたします。
ありがとうございました。

```html
<!DOCTYPE html>
<html lang="ja">
<head>
<meta charset="utf-8">
<title>だれでも週末から家庭菜園がはかどる</title>
<link rel="stylesheet" href="https://fonts.googleapis.com/css2?family=Noto+Serif+JP:wght@600;700;900&family=Noto+Sans+JP:wght@700;900&display=swap">
<style>
  :root {
    --bg: #e8ecf1;
    --glow: #fffdf4;
    --ink: #1d2a44;
    --rule: #b9c2cf;
    --art-warm: #f0b23a;
    --art-soft: #f4f2ec;
    --band-top: #8b3fa6;
    --band-bottom: #5b2577;
    --band-text: #ffffff;
    --band-accent: #ffe45a;
  }
  * { margin: 0; padding: 0; box-sizing: border-box; }
  html, body { width: 730px; height: 1200px; overflow: hidden; background: var(--bg); }
  .cover {
    position: relative;
    width: 730px;
    height: 1200px;
    background:
      radial-gradient(ellipse 380px 240px at 50% 230px, var(--glow) 0%, rgba(255,253,244,0.6) 45%, rgba(232,236,241,0) 100%),
      var(--bg);
    overflow: hidden;
    font-family: "Noto Serif JP", serif;
    color: var(--ink);
  }
  .title { position: absolute; left: 0; top: 22px; width: 730px; text-align: center; }
  .title-lead { font-size: 62px; font-weight: 700; letter-spacing: 1px; line-height: 1.2; }
  .title-main { margin-top: 10px; line-height: 1; white-space: nowrap; }
  .title-main .big { font-size: 140px; font-weight: 700; letter-spacing: 2px; }
  .title-main .particle { font-size: 62px; font-weight: 700; }
  .title-tail { margin-top: 18px; font-size: 104px; font-weight: 700; letter-spacing: 4px; line-height: 1; }
  .rule { position: absolute; left: 40px; right: 40px; top: 474px; height: 3px; background: var(--rule); }
  .illustration {
    position: absolute; left: 40px; top: 490px; width: 650px; height: 465px;
    background: radial-gradient(ellipse at 50% 55%, var(--art-warm) 0%, #f6d68f 40%, var(--art-soft) 75%, rgba(244,242,236,0) 100%);
    border-radius: 20px;
  }
  .author { position: absolute; left: 0; top: 968px; width: 730px; text-align: center; font-size: 54px; font-weight: 700; letter-spacing: 4px; }
  .author .role { font-size: 28px; letter-spacing: 0; margin-left: 4px; }
  .band { position: absolute; left: 0; top: 1056px; width: 730px; height: 144px; font-family: "Noto Sans JP", sans-serif; }
  .band-head {
    height: 60px; background: var(--band-top); color: var(--band-text);
    font-family: "Noto Serif JP", serif; font-weight: 700; font-size: 40px;
    text-align: center; line-height: 60px;
  }
  .band-body { height: 84px; background: var(--band-bottom); color: var(--band-accent); font-weight: 900; font-size: 29px; line-height: 38px; padding: 5px 0 0 34px; }
</style>
</head>
<body>
  <main class="cover">
    <h1 class="title">
      <div class="title-lead">だれでも週末から</div>
      <div class="title-main"><span class="big">家庭菜園</span><span class="particle">が</span></div>
      <div class="title-tail">はかどる</div>
    </h1>
    <div class="rule"></div>
    <div class="illustration" role="img" aria-label="Illustration: two people in yellow sweaters chatting cheerfully over papers at a desk, with speech bubbles"></div>
    <p class="author">柚木 瑛之助<span class="role">著</span></p>
    <section class="band">
      <div class="band-head">簡単に会議ができるTipsを集約</div>
      <div class="band-body">
        <p>用意しておくのは、アジェンダと終了条件だけ！</p>
        <p>オンライン会議にも対応！</p>
      </div>
    </section>
  </main>
</body>
</html>
```